Business card for plumber

I need a business card for my plumbing company.
on it should:
Surname
position
E-mail
Telephone & mobile phone
Website
Please everything as placeholders / fantasy names.
We stand for high quality, hygiene and professionalism.

Colours:
# 606060 anthracite
# f7931e orange
# 2b89cc blue

Industry/Entity Type

Plumber

Contact Information for Business Card

folgt...

```html
<!DOCTYPE html>
<html lang="en">
<head>
<meta charset="utf-8">
<title>Kessler Haustechnik – Business Card</title>
<link href="https://fonts.googleapis.com/css2?family=Lato:wght@400;700;900&display=swap" rel="stylesheet">
<style>
  :root {
    --blue: #2b89cc;
    --orange: #f7931e;
    --anthracite: #606060;
    --white: #ffffff;
    --stage: #3a3b3e;
  }
  * { margin: 0; padding: 0; box-sizing: border-box; }
  html, body {
    width: 1200px;
    height: 900px;
    overflow: hidden;
    background: var(--stage);
    font-family: 'Lato', sans-serif;
  }
  .stage {
    position: relative;
    width: 1200px;
    height: 900px;
  }
  .card {
    position: absolute;
    left: 290px;
    width: 620px;
    height: 354px;
    border-radius: 28px;
    overflow: hidden;
    box-shadow: 0 14px 34px rgba(0,0,0,0.45);
  }
  .card-front { top: 70px; background: var(--blue); }
  .card-back  { top: 476px; background: var(--white); }

  .brand {
    position: absolute;
    display: flex;
    align-items: center;
    gap: 12px;
    z-index: 1;
  }
  .brand-mark {
    width: 34px;
    height: 34px;
    background: var(--orange);
  }
  .brand-name {
    font-weight: 900;
    font-size: 30px;
    letter-spacing: 0.5px;
    line-height: 1;
    white-space: nowrap;
  }
  .card-front .brand {
    left: 0; right: 0; top: 158px;
    justify-content: center;
  }
  .card-front .brand-name { color: var(--white); }

  .card-back .brand { left: 48px; top: 150px; }
  .card-back .brand-name { color: var(--blue); font-size: 22px; }
  .card-back .brand-mark { width: 26px; height: 26px; }

  .back-art {
    position: absolute;
    inset: 0;
    width: 620px;
    height: 354px;
  }
  .wave-blue { fill: var(--blue); }
  .wave-orange { fill: var(--orange); }

  .person {
    position: absolute;
    right: 52px;
    top: 48px;
    text-align: right;
  }
  .person-name {
    color: var(--blue);
    font-weight: 700;
    font-size: 28px;
    letter-spacing: 0.3px;
    line-height: 1.1;
  }
  .person-role {
    color: var(--anthracite);
    font-size: 15px;
    margin-top: 4px;
  }

  .contacts {
    position: absolute;
    right: 26px;
    top: 198px;
    list-style: none;
    color: var(--white);
    font-size: 15px;
  }
  .contacts li {
    display: flex;
    justify-content: flex-end;
    align-items: center;
    gap: 12px;
    height: 24px;
  }
  .contacts svg {
    width: 16px;
    height: 16px;
    fill: none;
    stroke: var(--white);
    stroke-width: 1.6;
  }
</style>
</head>
<body>
<main class="stage">

  <section class="card card-front" aria-label="Card front">
    <div class="brand">
      <span class="brand-mark"></span>
      <span class="brand-name">KESSLER HAUSTECHNIK</span>
    </div>
  </section>

  <section class="card card-back" aria-label="Card back">
    <svg class="back-art" viewBox="0 0 620 354" aria-hidden="true">
      <path class="wave-blue" d="M0,354 L0,302 C180,302 300,282 385,212 C455,152 530,118 620,110 L620,354 Z"/>
      <path class="wave-orange" d="M40,286 C200,290 300,262 374,198 C442,138 492,114 542,104 C492,118 447,144 386,204 C312,272 200,300 40,298 Z"/>
    </svg>

    <div class="brand">
      <span class="brand-mark"></span>
      <span class="brand-name">KESSLER HAUSTECHNIK</span>
    </div>

    <div class="person">
      <p class="person-name">LUKAS BERGER</p>
      <p class="person-role">Managing partner</p>
    </div>

    <ul class="contacts">
      <li>+000 111 11 11
        <svg viewBox="0 0 16 16"><path d="M2 6 C2 3 14 3 14 6 L11 7 L10 5 L6 5 L5 7 Z"/><rect x="4" y="8" width="8" height="6" rx="1"/><circle cx="8" cy="11" r="1.3"/></svg>
      </li>
      <li>+000 111 11 11
        <svg viewBox="0 0 16 16"><rect x="4.5" y="1.5" width="7" height="13" rx="1.2"/><line x1="7" y1="12.5" x2="9" y2="12.5"/></svg>
      </li>
      <li>info@yourmail.com
        <svg viewBox="0 0 16 16"><rect x="1.5" y="3.5" width="13" height="9"/><path d="M1.5 3.5 L8 9 L14.5 3.5"/></svg>
      </li>
      <li>www.yourwebste.com
        <svg viewBox="0 0 16 16"><circle cx="8" cy="8" r="6.5"/><ellipse cx="8" cy="8" rx="3" ry="6.5"/><line x1="1.5" y1="8" x2="14.5" y2="8"/></svg>
      </li>
    </ul>
  </section>

</main>
</body>
</html>
```